B.S.L.H. Letterhead design

I would like a really professionally designed letterhead for my professional tutoring business called "The Bright Steps Learning Hub" (B.S.L.H.).Something fresh,modern and inspiring that will breath new life into the bu.The business/centre offers professional tutoring for 6 - 16 year olds in maths and english.

I have also attached a centre picture our logo, our proposed school bag,and our latest newsletter to give some perspective & background.

We like to see designs that use the blue & yellow colour theme.The final design should communicate ... "Giving Your Child A Secure Future ... And You Yourself ... Peace Of Mind!!!"

```html
<!DOCTYPE html>
<html lang="en">
<head>
<meta charset="UTF-8">
<title>B.S.L.H. Letterhead</title>
<link rel="stylesheet" href="https://fonts.googleapis.com/css2?family=Marcellus&family=Arimo&family=Open+Sans&display=swap">
<style>
  :root {
    --navy: #182b64;
    --gold: #f5c518;
    --paper: #ffffff;
    --frame: #8a8a8a;
    --body-text: #5a5a5a;
    --footer-text: #333333;
  }
  * { margin: 0; padding: 0; box-sizing: border-box; }
  html, body { width: 849px; height: 1200px; overflow: hidden; background: var(--paper); }
  .letterhead {
    position: relative;
    width: 849px;
    height: 1200px;
    background: var(--paper);
    border: 1px solid var(--frame);
    overflow: hidden;
  }
  .masthead {
    position: absolute;
    left: 0; top: 0;
    width: 100%;
    height: 155px;
    background: var(--navy);
  }
  .brand {
    position: absolute;
    left: 40px;
    top: 24px;
    width: 264px;
    text-align: center;
    color: var(--gold);
    font-family: "Marcellus", serif;
  }
  .brand-mark {
    display: flex;
    align-items: center;
    justify-content: center;
    gap: 12px;
    height: 66px;
  }
  .brand-square {
    width: 30px; height: 30px;
    background: var(--gold);
  }
  .brand-initials { font-size: 34px; letter-spacing: 2px; }
  .brand-site {
    margin-top: 11px;
    font-size: 16.5px;
    line-height: 20px;
    white-space: nowrap;
  }
  .brand-tagline {
    margin: 2px auto 0;
    width: 240px;
    border-top: 1px solid var(--gold);
    padding-top: 2px;
    font-size: 9px;
  }
  .masthead-name {
    position: absolute;
    right: 82px;
    top: 121px;
    color: var(--gold);
    font-family: "Marcellus", serif;
    font-size: 16px;
  }
  .letter-body {
    position: absolute;
    left: 98px;
    top: 265px;
    width: 653px;
    color: var(--body-text);
    font-family: "Arimo", Arial, sans-serif;
    font-size: 16.4px;
    line-height: 23.5px;
  }
  .salutation { margin-bottom: 47px; }
  .letter-body p.paragraph { text-align: justify; margin-bottom: 23.5px; }
  .contact-footer {
    position: absolute;
    left: 0; right: 0;
    top: 1141px;
    text-align: center;
    color: var(--footer-text);
    font-family: "Open Sans", Arial, sans-serif;
    font-size: 10.5px;
    line-height: 15px;
  }
  .base-band {
    position: absolute;
    left: 0; bottom: 0;
    width: 100%;
    height: 15px;
    background: var(--navy);
  }
</style>
</head>
<body>
<div class="letterhead">
  <header class="masthead">
    <div class="brand">
      <div class="brand-mark">
        <span class="brand-square"></span>
        <span class="brand-initials">B.S.L.H.</span>
      </div>
      <div class="brand-site">TheBrightStepsLearningHub.co.uk</div>
      <div class="brand-tagline">London's Leading Learning Centre</div>
    </div>
    <div class="masthead-name">The Bright Steps Learning Hub</div>
  </header>

  <main class="letter-body">
    <p class="salutation">Dear Sir,</p>
    <p class="paragraph">Lorem Ipsum is simply dummy text of the printing and typesetting industry. Lorem Ipsum has been the industry's standard dummy text ever since the 1500s, when an unknown printer took a galley of type and scrambled it to make a type specimen book. It has survived not only five centuries, but also the leap into electronic typesetting, remaining essentially unchanged. It was popularised in the 1960s with the release of Typeline sheets containing Lorem Ipsum passages, and more recently with desktop publishing software like Folio LayoutDesk including versions of Lorem Ipsum.</p>
    <p class="paragraph">Lorem Ipsum is simply dummy text of the printing and typesetting industry. Lorem Ipsum has been the industry's standard dummy text ever since the 1500s, when an unknown printer took a galley of type and scrambled it to make a type specimen book. It has survived not only five centuries, but also the leap into electronic typesetting, remaining essentially unchanged. It was popularised in the 1960s with the release of Typeline sheets containing Lorem Ipsum passages, and more recently with desktop publishing software like Folio LayoutDesk including versions of Lorem Ipsum.</p>
    <p class="paragraph">Lorem Ipsum is simply dummy text of the printing and typesetting industry. Lorem Ipsum has been the industry's standard dummy text ever since the 1500s, when an unknown printer took a galley of type and scrambled it to make a type specimen book.</p>
  </main>

  <footer class="contact-footer">
    <div>Add.:&nbsp; Your Commercial or office address • Ph.: 00.00.00.0000 • Fax: 00.00.00.0000</div>
    <div>Email: yourname@yourwebsite.com • Web.: www.yourwebsite.com</div>
  </footer>
  <div class="base-band"></div>
</div>
</body>
</html>
```